New Creative Busines Card

Hi Lead Designer,

How are you going?

I was hoping you can help me design the perfect business card for my new business. I have listed below some background information about the business and the concept to help with your design. I'm open to any form of creative ideas, but would like to have two types of colour schemes one dark color and one light.

I would like to have a dark set of design and a light (One design with one in black or dark background and one with light background to compare the contrast since the business card will be double sided one) I imagine this will be pretty easy to change the background of the design. Would prefer one side to have all the details and the other will just have a amazing logo (K7) to give it the finishing touch.

Feel free to email me if you have any questions.

Business Structure and design concepts:

Name of the business: K7 Advisory
Business: Dating agency and event management (Date night etc)
Concept: The main focus will be the K7 ( As some sort of a heart shape like logo) be creative
Details to include in the card will be general details like Name, Title: , Email, mobile, website (Contact details will be given later).

The rest of the idea is up to you, feel free to go crazy with your creative ideas.

Thank you for your help in advance, may the best candidate win~!

Target Market(s)

Target market will be Professional, Elegant, young and ambitious people.

Industry/Entity Type

Business

Requirements
Must have
• Focus on the K7 (as some sort of a heart shape logo). Since this is a double sides design would prefer on one side to focus on the just the K7 logo and the other side with a smaller version of the logo (with it or without) and all the details such as Name, Title, Mobile, Email, Website. Please have the design in landscape format.Not fuss with the Font as long as it is easy to read.
Nice to have
• Different Contrast in colours (keep it simple) one side dark colour scheme and one side light. Prefer to have 3-4 colours (not overwhelm with too many colours) to keep it simple and elegant.
Should not have
• Too colours, main focus is should be the K7 logo not the colours

```html
<!DOCTYPE html>
<html lang="en">
<head>
<meta charset="utf-8">
<title>K7 Advisory – Business Card</title>
<link href="https://fonts.googleapis.com/css2?family=Quattrocento:wght@400&display=swap" rel="stylesheet">
<style>
  :root {
    --plum: #8e2260;
    --plum-text: #8a2a5e;
    --blush-light: #fbf8fa;
    --blush-edge: #e6d7e0;
    --white: #ffffff;
    --white-soft: rgba(255, 255, 255, 0.82);
    --card-shadow: rgba(60, 30, 50, 0.28);
  }
  * { margin: 0; padding: 0; box-sizing: border-box; }
  html, body {
    width: 1200px;
    height: 980px;
    overflow: hidden;
    background: var(--white);
  }
  body {
    position: relative;
    font-family: "Quattrocento", Georgia, serif;
  }
  .card {
    position: absolute;
    left: 250px;
    width: 700px;
    height: 420px;
    box-shadow: 0 6px 18px var(--card-shadow);
    overflow: hidden;
  }
  .card--front {
    top: 50px;
    background: radial-gradient(ellipse at 50% 50%, var(--blush-light) 0%, var(--blush-light) 25%, var(--blush-edge) 100%);
    color: var(--plum-text);
  }
  .card--back {
    top: 510px;
    background: var(--plum);
    color: var(--white);
  }
  .brand {
    position: absolute;
    text-align: center;
    line-height: 1;
  }
  .brand__mark { display: block; }
  .brand__name { display: block; letter-spacing: 0.5px; }
  .card--front .brand { left: 60px; top: 52px; width: 260px; }
  .card--front .brand__mark { font-size: 38px; }
  .card--front .brand__name { font-size: 26px; margin-top: 6px; }
  .card--back .brand { left: 45px; top: 78px; width: 220px; }
  .card--back .brand__mark { font-size: 32px; }
  .card--back .brand__name { font-size: 21px; margin-top: 4px; }
  .brand-circle {
    position: absolute;
    border-radius: 50%;
  }
  .card--front .brand-circle {
    left: 100px;
    top: 140px;
    width: 180px;
    height: 180px;
    border: 5px solid var(--plum);
  }
  .card--back .brand-circle {
    left: 90px;
    top: 158px;
    width: 130px;
    height: 130px;
    border: 4px solid var(--white);
  }
  .services {
    position: absolute;
    left: 340px;
    top: 132px;
    width: 330px;
    text-align: center;
    font-size: 28px;
    line-height: 52px;
    text-transform: uppercase;
  }
  .contact {
    position: absolute;
    left: 330px;
    top: 82px;
  }
  .contact__name { font-size: 26px; line-height: 32px; }
  .contact__title {
    font-size: 18px;
    line-height: 24px;
    color: var(--white-soft);
    margin-bottom: 18px;
  }
  .contact__list { list-style: none; }
  .contact__item {
    display: flex;
    align-items: center;
    height: 40px;
    font-size: 23px;
  }
  .contact__icon {
    width: 20px;
    height: 20px;
    margin-right: 16px;
    flex: none;
  }
</style>
</head>
<body>

  <section class="card card--front">
    <div class="brand">
      <span class="brand__mark">K7</span>
      <span class="brand__name">ADVISORY</span>
    </div>
    <div class="brand-circle"></div>
    <p class="services">Dating Agency<br>and<br>Event Management</p>
  </section>

  <section class="card card--back">
    <div class="brand">
      <span class="brand__mark">K7</span>
      <span class="brand__name">ADVISORY</span>
    </div>
    <div class="brand-circle"></div>
    <div class="contact">
      <p class="contact__name">Name Surname</p>
      <p class="contact__title">Title</p>
      <ul class="contact__list">
        <li class="contact__item">
          <svg class="contact__icon" viewBox="0 0 20 20" aria-hidden="true"><path d="M4 2 L7 2 L8.5 6 L6.5 7.5 C7.5 10 10 12.5 12.5 13.5 L14 11.5 L18 13 L18 16 C18 17 17 18 16 18 C9 17.5 2.5 11 2 4 C2 3 3 2 4 2 Z" fill="var(--white)"/></svg>
          <span>123-456-7890</span>
        </li>
        <li class="contact__item">
          <svg class="contact__icon" viewBox="0 0 20 20" aria-hidden="true"><rect x="5" y="1.5" width="10" height="17" rx="1.5" fill="none" stroke="var(--white)" stroke-width="1.8"/><circle cx="10" cy="15.5" r="1" fill="var(--white)"/></svg>
          <span>123-456-7888</span>
        </li>
        <li class="contact__item">
          <svg class="contact__icon" viewBox="0 0 20 20" aria-hidden="true"><rect x="1.5" y="4.5" width="17" height="11" fill="none" stroke="var(--white)" stroke-width="1.8"/><path d="M1.5 4.5 L10 11 L18.5 4.5" fill="none" stroke="var(--white)" stroke-width="1.8"/></svg>
          <span>name@k7mail.com</span>
        </li>
        <li class="contact__item">
          <svg class="contact__icon" viewBox="0 0 20 20" aria-hidden="true"><circle cx="10" cy="10" r="8.5" fill="none" stroke="var(--white)" stroke-width="1.6"/><ellipse cx="10" cy="10" rx="3.6" ry="8.5" fill="none" stroke="var(--white)" stroke-width="1.4"/><path d="M1.5 10 H18.5 M3 5.5 H17 M3 14.5 H17" stroke="var(--white)" stroke-width="1.4"/></svg>
          <span>www.name.com</span>
        </li>
      </ul>
    </div>
  </section>

</body>
</html>
```